Fun, Clean Business Card For Family Focused Travel Agency

I need a business card using specific colors and fonts as in the uploaded files. Ideally, I would like a large image of the logo on the back and all the contact info on the front. Maybe the stars/dots somewhere in a flowy form.

I do want it the contact information to be clear and easy to read. I don't want it to look too busy. Maybe even a bit minimalist.

I plan or ordering the ROUNDED CORNER business cards from Cardwell Press, so please consider that in your design.

Target Market(s)

Families with children, couples, groups of friends

Contact Information for Business Card

Marla Quent, Owner
Marla@TidewayTrips.example
Cell Phone Number 555-218-6034
Office Phone Number 555-647-1295
Specializing in Fablecrest destinations, Goldmere Parkside Resort, Cruises and All-Inclusive Vacations.

Nice but not required:
www.TidewayTrips.example
Facebook, Instagram, Twitter icons with username: TidewayTrips

Font styles to use
Sans Serif

Requirements
Must have
• Please try to use the colors from the logo as much as possible. I understand lighter shades/colors may be needed for some things.
Should not have
• NO SERIF FONTS. That is really the only thing I do not want at all

```html
<!DOCTYPE html>
<html lang="en">
<head>
<meta charset="utf-8">
<title>Tideway Trips — Business Card</title>
<link href="https://fonts.googleapis.com/css2?family=Roboto:wght@400;500;700&display=swap" rel="stylesheet">
<style>
  :root{
    --stage:#f1f1f1;
    --sun:#fdd90a;
    --sun-light:#fff07a;
    --charcoal:#3a3a3a;
    --ink:#1d1d2c;
    --teal:#1fb5a8;
    --white:#ffffff;
  }
  *{margin:0;padding:0;box-sizing:border-box}
  html,body{width:1200px;height:1003px;overflow:hidden}
  body{background:var(--stage);font-family:"Roboto",Arial,sans-serif;position:relative}
  .card{position:absolute;border-radius:20px;overflow:hidden}
  .card-front{left:358px;top:168px;width:483px;height:275px;
    background:radial-gradient(ellipse at 50% 48%,var(--sun-light) 0%,var(--sun) 70%)}
  .card-back{left:358px;top:555px;width:484px;height:277px;display:flex}
  .brand{position:absolute;display:flex;align-items:center;gap:12px}
  .brand-dot{border-radius:50%;background:var(--teal);flex:none}
  .brand-name{font-weight:700;color:var(--ink);white-space:nowrap;letter-spacing:-0.5px}
  .card-front .brand{left:112px;top:108px}
  .card-front .brand-dot{width:56px;height:56px}
  .card-front .brand-name{font-size:35px}
  .back-brand{position:relative;width:242px;height:100%;flex:none;
    background:radial-gradient(ellipse at 45% 45%,var(--sun-light) 0%,var(--sun) 72%)}
  .back-brand .brand{left:44px;top:99px;gap:7px}
  .back-brand .brand-dot{width:32px;height:32px}
  .back-brand .brand-name{font-size:20px}
  .specialty{position:absolute;left:49px;top:161px;font-size:10.5px;line-height:13px;font-weight:500;color:var(--ink)}
  .contact{position:relative;flex:1;background:var(--charcoal);color:var(--white)}
  .contact-name{position:absolute;left:0;right:0;top:40px;text-align:center;font-size:29px;font-weight:700}
  .contact-web{position:absolute;left:0;right:0;top:73px;text-align:center;font-size:12.5px}
  .contact-list{position:absolute;left:32px;top:100px;list-style:none}
  .contact-list li{display:flex;align-items:center;height:29px;font-size:10.5px}
  .contact-list svg{width:20px;height:20px;margin-right:12px;flex:none}
  .contact-list b{font-weight:700;margin-left:4px}
  .social-rule{position:absolute;left:0;right:0;top:210px;height:2px;background:var(--sun)}
  .social{position:absolute;left:0;right:0;top:203px;display:flex;justify-content:center;gap:8px}
  .social span{width:16px;height:16px;border-radius:50%;background:var(--sun);border:2px solid var(--charcoal)}
  .social-handle{position:absolute;left:0;right:0;top:223px;text-align:center;font-size:12px;font-weight:700}
</style>
</head>
<body>
  <section class="card card-front" aria-label="Card front">
    <div class="brand"><span class="brand-dot"></span><span class="brand-name">Tideway Trips</span></div>
  </section>

  <section class="card card-back" aria-label="Card back">
    <div class="back-brand">
      <div class="brand"><span class="brand-dot"></span><span class="brand-name">Tideway Trips</span></div>
      <p class="specialty">Specializing in Fablecrest destinations,<br>Goldmere Parkside Resort,<br>Cruises and All-Inclusive Vacations.</p>
    </div>
    <div class="contact">
      <h1 class="contact-name">Marla Quent</h1>
      <p class="contact-web">www.TidewayTrips.example</p>
      <ul class="contact-list">
        <li><svg viewBox="0 0 20 20" fill="none" stroke="#fff" stroke-width="1.4"><rect x="2" y="5" width="16" height="11"/><path d="M2 5l8 6 8-6M2 16l6-5M18 16l-6-5"/></svg>Marla@TidewayTrips.example</li>
        <li><svg viewBox="0 0 20 20" fill="none" stroke="#fff" stroke-width="1.4"><rect x="3" y="3" width="5" height="14" rx="1"/><rect x="8" y="6" width="9" height="11" rx="1"/><path d="M10 9h5M10 12h1M12.5 12h1M10 14.5h1M12.5 14.5h1"/></svg>Office Phone<b>555-647-1295</b></li>
        <li><svg viewBox="0 0 20 20" fill="none" stroke="#fff" stroke-width="1.4"><rect x="6" y="2" width="8" height="16" rx="1.5" transform="rotate(-35 10 10)"/></svg>Cell Phone<b>555-218-6034</b></li>
      </ul>
      <div class="social-rule"></div>
      <div class="social" aria-label="Social profiles"><span></span><span></span><span></span></div>
      <p class="social-handle">TidewayTrips</p>
    </div>
  </section>
</body>
</html>
```